Logo and Business Card Design

Harbor Vale Logistics provides our customers with one call solutions to packing, trucking and warehousing needs throughout the supply chain.
We need ideas for a logo/business card. I have 2 general concepts.
1. Modern logo involving: the globe, Harbor Vale, arrow, movement, the two words having 2 different fonts/colors, the number 1.
2. Logo involving Lion/Winged Lion: incorporate lion onto globe, tagline "The Crest of the Herd", movement, flowing.

Target Market(s)

International Logistics companies, Air cargo companies, manufacturing companies

Industry/Entity Type

Business

Contact Information for Business Card

Dale Whitfield
Owner
Harbor Vale Logistics
2874 Maren Ave.
Elk Grove Village, IL 60029
847-539-2864
daleh@harborvalefreight.example

Font styles to use
Sans Serif

Requirements
Must have
• 1. Modern logo involving: the globe, Harbor Vale, arrow, movement, the two words having 2 different fonts/colors, the number 1.
Nice to have
Should not have
• Do not have too complex of a design.

```html
<!DOCTYPE html>
<html lang="en">
<head>
<meta charset="utf-8">
<title>Harbor Vale Logistics — Business Card</title>
<link rel="stylesheet" href="https://fonts.googleapis.com/css2?family=Open+Sans:wght@400;600;700&display=swap">
<style>
  :root {
    --backdrop: #e6e8eb;
    --card-white: #ffffff;
    --card-grey: #dcdee2;
    --blue-light: #1d9be0;
    --blue-mid: #2a6fd0;
    --blue-deep: #1f3f9e;
    --logo-blue: #2a5cc0;
    --text-on-blue: #ffffff;
  }
  * { margin: 0; padding: 0; box-sizing: border-box; }
  html, body {
    width: 1200px;
    height: 900px;
    overflow: hidden;
    background: var(--backdrop);
    font-family: "Open Sans", sans-serif;
  }
  .canvas {
    position: relative;
    width: 1200px;
    height: 900px;
  }
  .business-card {
    position: absolute;
    left: 100px;
    top: 164px;
    width: 1000px;
    height: 572px;
    border-radius: 56px;
    overflow: hidden;
    background: linear-gradient(100deg, var(--card-grey) 0%, var(--card-white) 30%, var(--card-white) 100%);
    box-shadow: 0 18px 40px rgba(0, 0, 0, 0.18);
  }
  .card-art {
    position: absolute;
    inset: 0;
    width: 1000px;
    height: 572px;
  }
  .brand {
    position: absolute;
    left: 48px;
    top: 250px;
    display: flex;
    align-items: center;
    gap: 14px;
  }
  .brand-mark {
    width: 34px;
    height: 34px;
    border-radius: 50%;
    background: var(--logo-blue);
  }
  .brand-name {
    font-weight: 700;
    font-size: 46px;
    letter-spacing: 0.5px;
    color: var(--logo-blue);
    line-height: 1;
  }
  .contact {
    position: absolute;
    right: 60px;
    top: 100px;
    text-align: right;
    color: var(--text-on-blue);
  }
  .contact-name {
    font-weight: 700;
    font-size: 35px;
    line-height: 1.15;
  }
  .contact-role {
    font-weight: 400;
    font-size: 30px;
    line-height: 1.1;
    margin-bottom: 30px;
  }
  .contact-line {
    font-size: 23px;
    line-height: 1.5;
  }
  .contact-web {
    font-size: 23px;
    line-height: 1.5;
    margin-top: 20px;
    margin-right: 18px;
  }
</style>
</head>
<body>
<main class="canvas">
  <section class="business-card">
    <svg class="card-art" viewBox="0 0 1000 572" aria-hidden="true">
      <defs>
        <radialGradient id="panelGlow" cx="0.55" cy="0.38" r="0.75">
          <stop offset="0" stop-color="var(--blue-light)"/>
          <stop offset="0.55" stop-color="var(--blue-mid)"/>
          <stop offset="1" stop-color="var(--blue-deep)"/>
        </radialGradient>
        <linearGradient id="swooshFill" x1="0" y1="0" x2="0" y2="1">
          <stop offset="0" stop-color="var(--blue-deep)"/>
          <stop offset="0.5" stop-color="var(--blue-mid)"/>
          <stop offset="1" stop-color="var(--blue-light)" stop-opacity="0.2"/>
        </linearGradient>
      </defs>
      <path class="info-panel" fill="url(#panelGlow)"
            d="M575 0 H1000 V572 H640 C505 520 455 390 460 270 C466 150 510 50 575 0 Z"/>
      <path class="accent-swoosh" fill="url(#swooshFill)"
            d="M545 12 C452 105 420 300 480 520 C452 360 462 170 545 12 Z"/>
    </svg>

    <div class="brand">
      <span class="brand-mark"></span>
      <span class="brand-name">Harbor Vale</span>
    </div>

    <div class="contact">
      <p class="contact-name">Dale Whitfield</p>
      <p class="contact-role">Owner</p>
      <p class="contact-line">2874 Maren Ave.</p>
      <p class="contact-line">Elk Grove Village, IL 60029</p>
      <p class="contact-line">P: 847-539-2864</p>
      <p class="contact-line">daleh@harborvalefreight.example</p>
      <p class="contact-web">www.harborvalefreight.example</p>
    </div>
  </section>
</main>
</body>
</html>
```